Tall ridge firewood

It a new firewood outlet in Jindabyne nsw that will only sell top hardwood firewood (ironbark , red gum, grey gum, an box mix. I would like to see a web page the we can do order online payment for delivery. It will all so need to have photos of the firewood. I all so have logo for tall ridge firewood
Must have a modem look but easy to use I would like to see a black back ground of some sort.

Here are some other firewood web pages for ideas and firewood info
http://www.kestrelfirewood.example.au
http://www.dunmorefirewood.example.au
http://www.wrenlogfirewood.example.au
http://www.tallisbluelogs.example.au/firewood

```html
<!DOCTYPE html>
<html lang="en">
<head>
<meta charset="utf-8">
<title>Tall Ridge Firewood</title>
<link href="https://fonts.googleapis.com/css2?family=Anton&family=Oswald:wght@500;700&family=Raleway:wght@400;500;600;700&display=swap" rel="stylesheet">
<style>
:root{
  --blue:#1c6bb8;
  --blue-light:#2f86d6;
  --ink:#25252b;
  --ink-deep:#1b1b20;
  --tan:#c59b6d;
  --white:#ffffff;
  --muted:#9a9aa2;
  --red:#c8181e;
  --wood-dark:#3a2417;
  --wood-mid:#7a4c2c;
}
*{margin:0;padding:0;box-sizing:border-box}
html,body{width:922px;height:1200px;overflow:hidden;background:var(--ink)}
body{position:relative;font-family:"Raleway",sans-serif;color:var(--white)}
.hero{position:absolute;left:0;top:0;width:922px;height:376px;background:radial-gradient(ellipse at 70% 40%,#8a5a36 0%,var(--wood-mid) 35%,var(--wood-dark) 100%)}
.topbar{position:absolute;left:0;top:26px;width:922px;height:40px;background:rgba(40,40,48,.85)}
.brand{position:absolute;left:0;top:0;width:360px;height:40px;background:var(--blue)}
.brand-name{position:absolute;left:26px;top:2px;font-family:"Anton",sans-serif;font-size:30px;line-height:36px;color:var(--white);letter-spacing:.5px}
.tagline{position:absolute;left:26px;top:44px;font-size:10px;letter-spacing:1.2px;color:var(--white);font-weight:600}
.nav{position:absolute;left:365px;top:0;height:40px;display:flex;list-style:none}
.nav li{font-family:"Oswald",sans-serif;font-weight:700;font-size:11.5px;line-height:40px;padding:0 10px;border-right:1px solid rgba(255,255,255,.1)}
.nav li.active{background:var(--ink-deep)}
.hotline-top{position:absolute;left:786px;top:0;font-family:"Oswald",sans-serif;font-weight:700;font-size:17px;line-height:40px;color:var(--blue-light);display:flex;align-items:center;gap:5px}
.headline{position:absolute;left:138px;top:150px;font-family:"Anton",sans-serif;font-size:41px;line-height:41px;text-transform:uppercase;letter-spacing:.5px;font-weight:400}
.slide-arrow{position:absolute;top:187px;width:48px;height:64px;background:rgba(255,255,255,.15);border:1px solid rgba(255,255,255,.4);display:flex;align-items:center;justify-content:center}
.slide-arrow.prev{left:0}.slide-arrow.next{right:0}
.welcome{position:absolute;left:0;top:376px;width:922px;height:380px;background:var(--ink)}
.welcome-title{position:absolute;left:138px;top:30px;font-family:"Anton",sans-serif;font-weight:400;font-size:20px;color:var(--blue-light);letter-spacing:.3px}
.welcome-title span{color:var(--blue)}
.welcome-copy{position:absolute;left:136px;top:78px;width:429px}
.video{position:relative;float:left;width:178px;height:142px;margin:2px 14px 10px 0;background:linear-gradient(#bbb 0,#bbb 16%,#2a1a12 16%,#c5461a 55%,#6b2a10 80%,#555 100%);border-radius:2px}
.play{position:absolute;left:68px;top:56px}
.lead{font-size:11.5px;line-height:15px;text-align:justify;margin-bottom:10px}
.body{font-size:10px;line-height:13px;color:var(--muted);text-align:justify}
.order{position:absolute;left:597px;top:329px;width:187px;height:378px;background:var(--tan);box-shadow:0 2px 6px rgba(0,0,0,.4)}
.order-head{height:47px;background:#2a2a31;font-family:"Anton",sans-serif;font-size:20px;color:var(--blue-light);text-align:center;line-height:50px}
.order-note{position:absolute;left:21px;top:58px;width:150px;font-size:8.5px;line-height:10.5px;color:#3b2a1c}
.field{position:absolute;left:21px;width:145px;height:19px;background:var(--white);border-radius:2px;font-size:8px;line-height:19px;color:#888;padding-left:9px}
.field .req{color:var(--red)}
.field.select::after{content:"";position:absolute;right:0;top:0;width:9px;height:19px;background:var(--ink-deep)}
.next-btn{position:absolute;left:21px;top:320px;width:146px;height:38px;background:var(--blue);font-family:"Anton",sans-serif;font-size:22px;line-height:38px;display:flex;align-items:center;justify-content:center;gap:8px}
.products{position:absolute;left:0;top:756px;width:922px;height:274px;background:linear-gradient(#fff,#f1f1f1)}
.products-title{position:absolute;left:0;top:26px;width:922px;text-align:center;font-family:"Anton",sans-serif;font-weight:400;font-size:21px;color:var(--blue)}
.products-title span{color:var(--ink)}
.carousel-btn{position:absolute;top:118px;width:20px;height:20px;border-radius:50%;background:#8a8a8a;display:flex;align-items:center;justify-content:center}
.card{position:absolute;top:79px;width:156px;text-align:center;color:#333}
.card-img{width:156px;height:91px}
.card-name{font-size:10.5px;font-weight:500;margin-top:10px}
.card-sub{font-size:6.5px;color:#777;margin-top:1px}
.card-price{font-size:11px;font-weight:700;color:var(--red)}
.card.featured .card-name{color:var(--blue)}
.card-frame{position:absolute;left:289px;top:66px;width:181px;height:161px;background:#f7f7f7;box-shadow:0 1px 6px rgba(0,0,0,.25)}
.footer{position:absolute;left:0;top:1030px;width:922px;height:170px;background:radial-gradient(ellipse at 75% 60%,#3a1c10 0%,#1a1410 55%,#111 100%)}
.f-title{position:absolute;top:40px;font-family:"Anton",sans-serif;font-weight:400;font-size:13px;color:var(--blue-light)}
.f-list{position:absolute;top:66px;list-style:none;font-size:7px;font-weight:700;line-height:15px}
.f-text{position:absolute;top:64px;font-size:8.5px;line-height:11.5px;color:#aaa}
.f-text a{color:var(--blue-light);text-decoration:none}
.f-brand{position:absolute;left:361px;top:108px;width:200px;text-align:center;font-family:"Anton",sans-serif;font-size:14px;color:var(--white)}
.f-tag{position:absolute;left:361px;top:128px;width:200px;text-align:center;font-size:5.5px;color:#ccc}
.f-copy{position:absolute;left:361px;top:148px;width:200px;text-align:center;font-size:7px;color:#aaa}
.f-phone{position:absolute;left:690px;top:64px;font-size:13.5px;line-height:17px}
</style>
</head>
<body>
<header class="hero" role="img" aria-label="Photo of stacked hardwood logs with a lumberjack mascot"></header>
<div class="topbar">
  <div class="brand"><div class="brand-name">TALL RIDGE FIREWOOD</div></div>
  <div class="tagline">WOOD THAT GETS YOU HOT AND LAST ALL NIGHT LONG</div>
  <ul class="nav">
    <li class="active">HOME</li><li>ABOUT US</li><li>PRODUCTS</li><li>ORDER ONLINE</li><li>FAQ</li><li>CONTACT US</li>
  </ul>
  <div class="hotline-top">
    <svg width="10" height="16" viewBox="0 0 10 16"><rect x="1" y="1" width="8" height="14" rx="1.5" fill="none" stroke="#2f86d6" stroke-width="1.5"/><circle cx="5" cy="12.5" r="1" fill="#2f86d6"/></svg>
    0438 210 657
  </div>
</div>
<h1 class="headline">Delivering top<br>quality seasoned<br>hardwood all<br>year round</h1>
<div class="slide-arrow prev"><svg width="16" height="22" viewBox="0 0 16 22"><path d="M12 3 4 11l8 8" fill="none" stroke="#fff" stroke-width="4"/></svg></div>
<div class="slide-arrow next"><svg width="16" height="22" viewBox="0 0 16 22"><path d="M4 3l8 8-8 8" fill="none" stroke="#fff" stroke-width="4"/></svg></div>

<section class="welcome">
  <h2 class="welcome-title">WELCOME <span>TO OUR NEW ONLINE STORE</span></h2>
  <div class="welcome-copy">
    <div class="video" role="img" aria-label="Video still of a fire burning in a wood heater">
      <svg class="play" width="42" height="42" viewBox="0 0 42 42"><circle cx="21" cy="21" r="19" fill="#1c6bb8" stroke="#fff" stroke-width="3"/><path d="M16 12l13 9-13 9z" fill="#fff"/></svg>
    </div>
    <p class="lead">This is Layoutcraft's version of Lorem Ipsum. Proin gravida nibh vel velit auctor aliquet. Aenean sollicitudin, lorem quis bibendum auctor, nisi elit consequat ipsum, nec sagittis sem nibh id elit.</p>
    <p class="body">This is Layoutcraft's version of Lorem Ipsum. Proin gravida nibh vel velit auctor aliquet. Aenean sollicitudin, lorem quis bibendum auctor, nisi elit consequat ipsum, nec sagittis sem nibh id elit. Duis sed odio sit amet nibh vulputate cursus a sit amet tincidunt auctor a ornare odio. Sed non mauris vitae erat consequat auctor eu in elit. Class aptent taciti sociosqu ad litora torquent per conubia nostra, per inceptos himenaeos. Mauris in erat justo. Nullam ac urna eu felis dapibus condimentum sit amet a augue. Sed non neque elit. Sed ut imperdiet nisi. Proin condimentum fermentum nunc. Etiam pharetra, erat sed fermentum feugiat, velit mauris egestas quam, ut aliquam massa nisl quis neque. Suspendisse in orci enim. This is Layoutcraft's version of Lorem Ipsum. Proin gravida nibh vel velit auctor aliquet. Aenean sollicitudin, lorem quis bibendum auctor.</p>
  </div>
</section>

<form class="order">
  <div class="order-head">ORDER FIREWOOD</div>
  <p class="order-note">Fill out the form below to order your firewood delivery. Deliveries are usually between <b>4:00PM &amp; 9:00PM</b> Can take up to 2 weeks to deliver (especially in the off session)</p>
  <div class="field" style="top:126px">Email <span class="req">*</span></div>
  <div class="field" style="top:149px">Phone</div>
  <div class="field" style="top:172px">Address <span class="req">*</span></div>
  <div class="field" style="top:195px">Zip Code/City <span class="req">*</span></div>
  <div class="field" style="top:218px">Gate Code (if needed)</div>
  <div class="field select" style="top:241px">Firewood Type</div>
  <div class="field select" style="top:264px">Order Size</div>
  <div class="field select" style="top:287px">Kindling</div>
  <div class="next-btn">NEXT <svg width="16" height="16" viewBox="0 0 16 16"><circle cx="8" cy="8" r="7" fill="#fff"/><path d="M4 8h6M7.5 5l3 3-3 3" fill="none" stroke="#1c6bb8" stroke-width="2"/></svg></div>
</form>

<section class="products">
  <h2 class="products-title">NEW PRODUCTS FOR <span>FEBRUARY</span></h2>
  <div class="carousel-btn" style="left:100px"><svg width="8" height="10" viewBox="0 0 8 10"><path d="M6 1 2 5l4 4" fill="none" stroke="#fff" stroke-width="2"/></svg></div>
  <div class="carousel-btn" style="left:798px"><svg width="8" height="10" viewBox="0 0 8 10"><path d="M2 1l4 4-4 4" fill="none" stroke="#fff" stroke-width="2"/></svg></div>
  <div class="card-frame"></div>
  <div class="card" style="left:137px"><div class="card-img" role="img" aria-label="Photo of split mixed hardwood" style="background:linear-gradient(135deg,#d9a26a,#8a5230)"></div><div class="card-name">MIXED HARDWOOD</div><div class="card-sub">PICK-UP TRUCK LOAD</div><div class="card-price">$25.00</div></div>
  <div class="card featured" style="left:301px"><div class="card-img" role="img" aria-label="Photo of unsplit round logs" style="background:linear-gradient(135deg,#b59576,#5e4330)"></div><div class="card-name">UNSPLIT WOOD</div><div class="card-sub">STARTING AT</div><div class="card-price">$1.00 A LOG</div></div>
  <div class="card" style="left:469px"><div class="card-img" role="img" aria-label="Photo of a bunch of kindling" style="background:linear-gradient(135deg,#e2a36a,#a2602f)"></div><div class="card-name">BUNCH OF KINDLING</div><div class="card-sub">1 FOR</div><div class="card-price">$10.00</div></div>
  <div class="card" style="left:629px"><div class="card-img" role="img" aria-label="Photo of plain wood mulch" style="background:linear-gradient(135deg,#b8ab96,#6e6252)"></div><div class="card-name">PLAIN WOOD MULCH</div><div class="card-sub">PICK-UP TRUCK LOAD</div><div class="card-price">$25.00</div></div>
</section>

<footer class="footer">
  <h3 class="f-title" style="left:138px">NAVIGATION</h3>
  <ul class="f-list" style="left:138px"><li>HOME</li><li>ABOUT US</li><li>OUR PRODUCTS</li><li>FIREWOOD</li><li>FENCING</li></ul>
  <h3 class="f-title" style="left:231px">CONTACT US</h3>
  <p class="f-text" style="left:231px">Tall Ridge Firewood LTD.<br>14 Kosciuszko Road Jindabyne,<br>NSW 2627<br><a href="#">contact@tallridgefirewood.example.au</a></p>
  <div class="f-brand">TALL RIDGE FIREWOOD</div>
  <div class="f-tag">WOOD THAT GETS YOU HOT AND LAST ALL NIGHT LONG</div>
  <div class="f-copy">Copyrights © 2014, &nbsp;All rights Reserved</div>
  <h3 class="f-title" style="left:567px">HOURS:</h3>
  <ul class="f-list" style="left:567px"><li>MON-THUR 8:00AM-8:00PM</li><li>FRIDAY 8:00AM-4:00PM</li><li>SATURDAY CLOSED ALL DAY</li><li>SUNDAY 8:00AM-7:00PM</li></ul>
  <h3 class="f-title" style="left:690px">ENQUIRY HOTLINE</h3>
  <p class="f-phone">02 6456 0184<br>0412 733 905</p>
</footer>
</body>
</html>
```